Creative Magazine Ad - fusing comfort, culture and cuisine for a food supply company

Hello and welcome to this project!

We need an ad for our company, Larder Vale PNG, that is going to be in a magazine read by the Australian Army based in Papua New Guinea.

We want an ad that makes people stop and look. The key message is that even though Papua New Guinea is exotic, the food can be the same (as in Australia). And we want to show off what our company does – supplying great food that caters for all.

Your design should include:

Size:
• 1 page at 15cm height x 19.6cm width
Pictures:
• Our logo – Larder Vale PNG – where people can see it
• Pictures or elements that capture the tropical landscape, tribal culture and or essence of Papua New Guinea mixed with pictures of Australian food like barbeque, steaks, pies, roast vegetables etc.
Text to add:
• Title: "Taste of Home in the Tropics: Your Australian Culinary Guide in Papua New Guinea”
• Message: "Our mission is to manufacture and procure a diverse range of high-quality food products, catering to the unique needs of defence camps, and supplying small to large wholesalers, retailers, restaurants, hotels, and caterers throughout Papua New Guinea. We are dedicated to supporting our defence forces with the comforts of home, while serving the broader community with exceptional culinary offerings."
• And our contact details:
+675 341 6092
www.lvx.com.pg
sales@lardervalepng.com.pg

What we need:
• A graphic for printing for the magazine.
• A digital version to use online.

Thanks again – any questions please ask :)

A Bit About Us
Larder Vale PNG Ltd is a 100% PNG-owned and managed business and is proud to be one of the largest food supply companies in the country. Our ability to supply a wide range of premium imported, local and in-house manufactured products from our Butchery and Bakery has contributed to the rock-solid reputation for quality and services that Larder Vale now enjoys throughout PNG.

We are proud to also sell our wide range of products through our retail outlets (Gudi Grill Stoa, Gudi Crust Stoa and Tiki Grill Stoa) and our popular Quick Service Restaurants (Heron Wrapper and Kelo Tart Jar). Our Catering division (Gudi Rofa Catering) owns a vast array of commercial catering equipment and has experience catering for large-scale events in PNG. We are the only company in Papua New Guinea that has the technology to provide “tamper proof” cold and hot individual meal solutions that can be delivered in temperature-controlled vehicles to locations in Port Moresby but also as a solution to large-scale mining camp catering needs.

```html
<!DOCTYPE html>
<html lang="en">
<head>
<meta charset="utf-8">
<title>Larder Vale PNG – Taste of Home in the Tropics</title>
<link rel="stylesheet" href="https://fonts.googleapis.com/css2?family=Alegreya+Sans:wght@500;700&family=Abel&family=Montserrat:wght@600&family=Arimo:ital,wght@1,700&display=swap">
<style>
  :root {
    --red: #f21c1f;
    --ink: #111111;
    --green: #8fad72;
    --paper: #ffffff;
    --tomato: #d8372a;
    --corn: #f0b340;
    --glaze: #8a3a1e;
    --char: #3a1a10;
  }
  * { margin: 0; padding: 0; box-sizing: border-box; }
  html, body { width: 1200px; height: 918px; overflow: hidden; background: var(--paper); }
  .ad { position: relative; width: 1200px; height: 918px; overflow: hidden; background: var(--paper); }

  .page-card {
    position: absolute; left: 186px; top: 45px; width: 816px; height: 814px;
    background: var(--paper);
    box-shadow: 4px 6px 14px rgba(0,0,0,0.35);
  }
  .diagonal-band { position: absolute; inset: 0; width: 1200px; height: 918px; }

  .brand { position: absolute; left: 214px; top: 88px; display: flex; align-items: center; gap: 9px; }
  .brand-dot { width: 20px; height: 20px; border-radius: 50%; background: var(--ink); flex: none; }
  .brand-name {
    font-family: "Alegreya Sans", sans-serif; font-weight: 700; font-size: 40px;
    color: var(--ink); line-height: 1; white-space: nowrap;
  }
  .cert-badge { position: absolute; left: 342px; top: 63px; width: 54px; height: 20px; background: var(--ink); border-radius: 3px; }
  .brand-tagline {
    position: absolute; left: 222px; top: 177px;
    font-family: "Arimo", sans-serif; font-style: italic; font-weight: 700; font-size: 11px;
    color: var(--ink); white-space: nowrap;
  }

  .headline {
    position: absolute; right: 231px; top: 187px;
    font-family: "Alegreya Sans", sans-serif; font-weight: 500; font-size: 49px;
    color: var(--red); white-space: nowrap; line-height: 1;
  }
  .subhead {
    position: absolute; right: 229px; top: 243px; text-align: right;
    font-family: "Abel", sans-serif; font-size: 26px; line-height: 29px;
    color: var(--green); text-transform: uppercase; white-space: nowrap;
  }

  .food-photo {
    position: absolute; left: 228px; top: 324px; width: 741px; height: 378px;
    clip-path: polygon(4% 62%, 8% 57%, 22% 55%, 26% 40%, 40% 38%, 50% 20%, 68% 0%, 73% 6%, 78% 12%, 80% 16%, 82% 25%, 91% 30%, 95% 41%, 100% 52%, 96% 61%, 86% 70%, 80% 76%, 75% 74%, 63% 86%, 46% 100%, 36% 92%, 28% 94%, 17% 88%, 11% 74%);
    background: linear-gradient(115deg, var(--tomato) 5%, var(--corn) 38%, var(--glaze) 55%, var(--char) 78%, var(--glaze) 100%);
  }

  .contact {
    position: absolute; left: 211px; top: 762px; font-style: normal;
    font-family: "Alegreya Sans", sans-serif; font-weight: 500; font-size: 23px;
    letter-spacing: 1.6px; line-height: 27px; color: var(--red);
  }

  .mission {
    position: absolute; left: 1034px; top: 852px; width: 800px; height: 130px;
    transform: rotate(-90deg); transform-origin: top left;
    font-family: "Montserrat", sans-serif; font-weight: 600; font-size: 14.6px;
    letter-spacing: 1.5px; line-height: 21.5px; color: var(--green);
    text-align: justify;
  }
</style>
</head>
<body>
<main class="ad">
  <div class="page-card"></div>

  <svg class="diagonal-band" viewBox="0 0 1200 918" aria-hidden="true">
    <polygon points="0,0 36,0 1200,798 1200,918 840,918 0,360" fill="var(--red)"/>
  </svg>

  <div class="brand">
    <span class="brand-dot"></span>
    <span class="brand-name">Larder Vale</span>
  </div>
  <div class="cert-badge" aria-hidden="true"></div>
  <p class="brand-tagline">“100% PNG Owned &amp; Operated”</p>

  <h1 class="headline">Taste of Home in the Tropics</h1>
  <p class="subhead">Your Australian Culinary<br>Guide in Papua New Guinea</p>

  <div class="food-photo" role="img" aria-label="Photo of glazed barbecued ribs with rosemary, grilled corn cobs, a roasted garlic bulb, a halved tomato and a bowl of barbecue sauce"></div>

  <address class="contact">
    +675 341 6092<br>
    www.lvx.com.pg<br>
    sales@lardervalepng.com.pg
  </address>

  <p class="mission">Our mission is to manufacture and procure a diverse range of high-quality food products, catering to the unique needs of defence camps, and supplying small to large wholesalers, retailers, restaurants, hotels, and caterers throughout Papua New Guinea. We are dedicated to supporting our defence forces with the comforts of home, while serving the broader community with exceptional culinary offerings.</p>
</main>
</body>
</html>
```